Outdoor sign for Brindle Auto Restoration

I need a horizontal 4'x 8' outdoor roadside sign for my classic auto restoration business. I have uploaded colors and our logo. Needs the Brindle name, a prominent Classic AUTO RESTORATION, phone number and website. We rebuild and restore vintage cars, trucks and 4x4s. I'd like something clean but possibly retro. Classic Auto Restoration is more important than the Brindle name. It needs to be visible and readable from the street. NO CLIP ART

Target Market(s)

Customers who need their vintage care restored or upgraded. Men and women ages 25-75

Industry/Entity Type

Automotive

Colors
FFC000
F8CF3A
FAE287
FDF2CF
FEFAEE

Requirements
Must have
• Legible. Bright. Readable as a backlit 4' x 8' large horizontal sign (roughly 120cm X 240cm)
Nice to have
• Use of the Brindle logo/type, Complete or Classic before prominent AUTO RESTORATION
Should not have
• Clip art of old cars or icons. And we don't want the Brindle Logo from the website because it wont be legible from the road. I have included the Illustrator file for Brindle text in the uploads

```html
<!DOCTYPE html>
<html lang="en">
<head>
<meta charset="utf-8">
<title>Brindle Auto Restoration – Roadside Sign</title>
<link rel="stylesheet" href="https://fonts.googleapis.com/css2?family=Anton&family=Roboto+Condensed:wght@700&display=swap">
<style>
  :root {
    --page-bg: #e6e6e6;
    --stripe-light: #4a4a4a;
    --stripe-dark: #232323;
    --gold-top: #fae287;
    --gold-mid: #ffc000;
    --gold-deep: #f29a0b;
    --outline: #2a1a06;
    --bar-black: #0c0c0c;
    --contact-text: #fefaee;
    --star: #ffe400;
  }
  * { margin: 0; padding: 0; box-sizing: border-box; }
  html, body {
    width: 1200px;
    height: 1121px;
    overflow: hidden;
    background: var(--page-bg);
  }
  .sign {
    position: absolute;
    left: 50px;
    top: 285px;
    width: 1100px;
    height: 550px;
    background: repeating-linear-gradient(90deg, var(--stripe-light) 0 84.615px, var(--stripe-dark) 84.615px 169.23px);
    box-shadow: 0 2px 6px rgba(0,0,0,.25);
  }
  .sign-art { position: absolute; inset: 0; width: 100%; height: 100%; }
  .headline {
    font-family: "Anton", "Impact", sans-serif;
    fill: url(#goldText);
    stroke: var(--outline);
    stroke-width: 8px;
    stroke-linejoin: round;
    paint-order: stroke fill;
  }
  .contact {
    font-family: "Roboto Condensed", "Arial Narrow", sans-serif;
    font-weight: 700;
    font-size: 28px;
    fill: var(--contact-text);
  }
  .star { fill: var(--star); }
</style>
</head>
<body>
<div class="sign">
  <svg class="sign-art" viewBox="0 0 1100 550" xmlns="http://www.w3.org/2000/svg">
    <defs>
      <linearGradient id="goldText" x1="0" y1="0" x2="0" y2="1">
        <stop offset="0" stop-color="var(--gold-top)"/>
        <stop offset="0.45" stop-color="var(--gold-mid)"/>
        <stop offset="1" stop-color="var(--gold-deep)"/>
      </linearGradient>
      <linearGradient id="marqueeTone" x1="0" y1="0" x2="0" y2="1">
        <stop offset="0" stop-color="var(--gold-mid)" stop-opacity="0.55"/>
        <stop offset="1" stop-color="var(--gold-deep)" stop-opacity="0.35"/>
      </linearGradient>
      <linearGradient id="barFade" x1="0" y1="0" x2="1" y2="0">
        <stop offset="0" stop-color="var(--bar-black)" stop-opacity="0"/>
        <stop offset="0.2" stop-color="var(--bar-black)"/>
        <stop offset="0.8" stop-color="var(--bar-black)"/>
        <stop offset="1" stop-color="var(--bar-black)" stop-opacity="0"/>
      </linearGradient>
      <linearGradient id="ruleFade" x1="0" y1="0" x2="1" y2="0">
        <stop offset="0" stop-color="var(--gold-mid)" stop-opacity="0"/>
        <stop offset="0.5" stop-color="var(--gold-mid)"/>
        <stop offset="1" stop-color="var(--gold-mid)" stop-opacity="0"/>
      </linearGradient>
      <symbol id="star" viewBox="-1 -1 2 2">
        <polygon class="star" points="0,-1 0.235,-0.324 0.951,-0.309 0.38,0.124 0.588,0.809 0,0.4 -0.588,0.809 -0.38,0.124 -0.951,-0.309 -0.235,-0.324"/>
      </symbol>
    </defs>

    <rect class="marquee-area" x="176" y="18" width="748" height="165" rx="80"
          fill="url(#marqueeTone)" role="img"
          aria-label="Retro gold marquee frame with light bulbs and curled ends framing the business name"/>

    <text class="headline brand-name" x="550" y="142" font-size="76" text-anchor="middle" textLength="330" lengthAdjust="spacingAndGlyphs">BRINDLE</text>

    <g class="title-stars">
      <use href="#star" x="408" y="188" width="24" height="24"/>
      <use href="#star" x="461" y="184" width="32" height="32"/>
      <use href="#star" x="522" y="172" width="54" height="54"/>
      <use href="#star" x="602" y="184" width="32" height="32"/>
      <use href="#star" x="663" y="188" width="24" height="24"/>
    </g>

    <text class="headline title-main" x="550" y="348" font-size="140" text-anchor="middle" textLength="552" lengthAdjust="spacingAndGlyphs">CLASSIC</text>
    <text class="headline title-sub" x="550" y="440" font-size="94" text-anchor="middle" textLength="820" lengthAdjust="spacingAndGlyphs">AUTO RESTORATION</text>

    <g class="star-rule">
      <use href="#star" x="28" y="451" width="24" height="24"/><use href="#star" x="67" y="451" width="24" height="24"/>
      <use href="#star" x="106" y="451" width="24" height="24"/><use href="#star" x="146" y="451" width="24" height="24"/>
      <use href="#star" x="185" y="451" width="24" height="24"/><use href="#star" x="224" y="451" width="24" height="24"/>
      <use href="#star" x="263" y="451" width="24" height="24"/><use href="#star" x="302" y="451" width="24" height="24"/>
      <use href="#star" x="342" y="451" width="24" height="24"/><use href="#star" x="381" y="451" width="24" height="24"/>
      <use href="#star" x="420" y="451" width="24" height="24"/><use href="#star" x="459" y="451" width="24" height="24"/>
      <use href="#star" x="498" y="451" width="24" height="24"/><use href="#star" x="538" y="451" width="24" height="24"/>
      <use href="#star" x="577" y="451" width="24" height="24"/><use href="#star" x="616" y="451" width="24" height="24"/>
      <use href="#star" x="655" y="451" width="24" height="24"/><use href="#star" x="694" y="451" width="24" height="24"/>
      <use href="#star" x="734" y="451" width="24" height="24"/><use href="#star" x="773" y="451" width="24" height="24"/>
      <use href="#star" x="812" y="451" width="24" height="24"/><use href="#star" x="851" y="451" width="24" height="24"/>
      <use href="#star" x="890" y="451" width="24" height="24"/><use href="#star" x="930" y="451" width="24" height="24"/>
      <use href="#star" x="969" y="451" width="24" height="24"/><use href="#star" x="1008" y="451" width="24" height="24"/>
      <use href="#star" x="1047" y="451" width="24" height="24"/>
    </g>

    <g class="contact-bar">
      <rect x="80" y="490" width="940" height="56" fill="url(#barFade)"/>
      <rect x="120" y="489" width="860" height="2" fill="url(#ruleFade)"/>
      <g class="icon-phone">
        <circle cx="238" cy="518" r="14" fill="var(--gold-mid)"/>
        <path d="M232 510 q-3 2 -2 6 q3 8 10 11 q4 1 6 -2 l-3 -3 q-2 1 -3 1 q-4 -2 -6 -6 q0 -1 1 -3 z" fill="var(--bar-black)"/>
      </g>
      <text class="contact phone" x="262" y="528">501 555 0142</text>
      <g class="icon-web" fill="none" stroke="var(--bar-black)" stroke-width="1.8">
        <circle cx="543" cy="518" r="14" fill="var(--gold-mid)" stroke="none"/>
        <circle cx="543" cy="518" r="9"/>
        <ellipse cx="543" cy="518" rx="4" ry="9"/>
        <line x1="534" y1="518" x2="552" y2="518"/>
      </g>
      <text class="contact website" x="567" y="528">brindleautoworks.com</text>
    </g>
  </svg>
</div>
</body>
</html>
```